Tumbler Cafe - Menu Redesign

What We Want

We're looking for a bold redesign of our current menu. Our current menu is tired and boring and does not accurately reflect our revitalization of the Tumbler Cafe brand. Attachments will be submitted with the campaign for menu items.

Design Guidelines

• Creative use of typography and color. Think Bold, Fun, Loud and uninhibited.
• Fluid, easy to read, layout that emphasizes readability.
• The subtle, demure, look of typographic columns (examples below in resources)
• Creative use of 'wells' for menu item highlights as well as great boarders
• Loud typefaces as long as readability is the focus & emphasis.
• Small illustrations/icons but they must not effect or take the focus from the readability of the menu
• Big, oversized, menu that will look great on recycled paper
• Subtle watermarks/illustrations
• creative use of textures / highlights / section breaks

Menu Requirements

• 9”x12” paper size. Please notify us if your design works better in a different format.
• Oversized, designed for printing on recycled paper.
• Single Page Menu (use lunch on front and breakfast on back)
• Do not use $ or "..." in pricing. Please space all prices equally.
• Simplistic layout that emphasizes readability and logical navigation of menu items.
• Acceptable file types
• Photoshop
• Indesign
• illustrator
• Please contact us before you submit a design if you plan on using something else
• HTML/CSS would be a huge benefit. It's not a must, but it will definitely help you win the award.
• Must retain some of our current color scheme (red/orange/yellow – see attachments/website).

NOTE: Please download ALL attached resources for the project.
Updates

Current web site:  www.tumblercafe-example.com

please read attachment:  tumbler_menu_redesign_request.docx

Lots of good information & examples on menus we like and the design elements featured in the menu.

All,

Thanks for your design submissions!  With all the designs that have be submitted so far, we are confident that our money will be well spent.  I have changed the project to non-refundable.  Please continue working on your designs using the design_request doc that's posted for guidelines/requirements.  I will provide specific feedback to designs as needed.

For your convenience:

Design Guidelines

 

Creativeuse of typography and color.  Think Bold,Fun, Loud and uninhibited.

Fluid,easy to read, layout that emphasizes readability.

Thesubtle, demure, look of typographic columns (examples below in resources)

Creativeuse of 'wells' for menu item highlights as well as great boarders

Loudtypefaces as long as readability is the focus & emphasis.

Smallillustrations/icons but they must not effect or take the focus from thereadability of the menu

Big,oversized, menu that will look great on recycled paper

Subtlewatermarks/illustrations

creativeuse of textures / highlights / section breaks

 

  MenuRequirements

 

9”x12”paper size.  Please notify us if yourdesign works better in a different format.

Oversized,designed for printing on recycled paper.

SinglePage Menu (use lunch on front and breakfast on back)

Donot use $ or "..." in pricing.Please space all prices equally.

Simplisticlayout that emphasizes readability and logical navigation of menu items.

Acceptablefile types

Photoshop

Indesign

illustrator 

Pleasecontact us before you submit a design if you plan on using something else

HTML/CSSwould be a huge benefit.  It's not amust, but it will definitely help you win the award.

Mustretain some of our current color scheme (red/orange/yellow – seeattachments/website). 

 

Do Not Use

 

Skeuomorphismin any way.

Wedo not want any actual pictures of food on the menu (subtle illustrations /icons are great and encouraged).

Typefacesthat are hard to read.

Thanks!

dana

Reason: need to incorporate changes to menu / menu items

Please expect some new copy tonight (USA EST) for the breakfast menu items.  Thanks!

dana

COPY UPDATE:  Please check new menu item listing (revision 3) for updated copy.  Please revisit all menu items as I have grouped, consolidated, and eliminated some items.

Thanks!

dana 

DESIGN UPDATE:  I added an omelette hero/jumbotron design that we'd like to use to display the omelettes on the breakfast menu.  It doesn't have to be exactly like this one, it's just meant to be a guideline.  Please take a look and see if you can fit it in to your design.  Also, the copy has been updated for the breakfast & lunch menus.

Reason: Revised design changes not yet received.

Reason: Designer needs more tine to complete final submission. This will be the last extension. Thanks! dana

Target Market(s)

Women - 60% or more. Mostly professionals. 18-55.
Men - Professionals mostly. Judges, Attorneys, Agents, Ect. Ages 18-55.

Industry/Entity Type

Printing

Colors
f37022
ec1f27
f78f20
faa54b
f04a50
fee18a
faee3e

Requirements
Must have
• see menu requirements in task description.
Nice to have
• Design Ideas We Love

http://www.menugallery-example.com/menucraft/archives/stonegate_inn.php
We like: typefaces, typographic columns & layout, use of butcher-block print, simplicity
We don't like: lack of bold, color lack of textures, lack of general vitality in the brand, no use of icons/illustrations

http://www.menugallery-example.com/menucraft/archives/patty_vault.php
We like: typefaces, bold headers & section breaks, texturized typefaces, use of illustrations, and specifically we love how they did the 'custom creation' menu
We don't like: lack of bold color, lack of subtle texturing, little more use of illustrated icons would be nice

http://www.menugallery-example.com/menucraft/archives/the_rowdy_roost.php
We like: use of bold colors, organization & layout, the section highlights are nice
We don't like: lack of textures, lack subtle illustrations/icons.

http://www.menugallery-example.com/menucraft/archives/wexford_mill.php
We like: use of textures, typefaces, layout & organization, single page menu
We don't like: lack of textures, lack of bold color, lack of icons and menu item hightlights

http://www.menugallery-example.com/menucraft/archives/zibbo_caf.php
We like: use of texturing, typesfaces, layout & organization, creative use of illustrations/icons, bold colors
We don't like: not a huge fan of the bordering; and illustrations take up too much room for single page menu

http://www.menugallery-example.com/menucraft/archives/ved_hjornet_af_torvet.php
We like: creative use of typefaces, organization & layout, cool illustrations, oversized menu, section seperators are cool & unique
We don't like: lack of textures, menu items inside illustrations, typefaces can get hard to read in certain areas
Should not have
• Do Not Use

• Skeuomorphism in any way.
• We do not want any actual pictures of food on the menu (subtle illustrations / icons are great and encouraged).
• Typefaces that are hard to read.

```html
<!DOCTYPE html>
<html lang="en">
<head>
<meta charset="utf-8">
<title>Tumbler Cafe Menu</title>
<link href="https://fonts.googleapis.com/css2?family=Oswald:wght@400;500;700&family=PT+Sans+Narrow:wght@400;700&display=swap" rel="stylesheet">
<style>
:root{
  --orange:#f37022;
  --orange-light:#f78f20;
  --red:#ec1f27;
  --blue:#1e6cc0;
  --yellow:#fed20c;
  --sage:#c8c4a0;
  --peach:#f9b99b;
  --cream:#fde3b3;
  --cream-light:#fee8bf;
  --ink:#231f1a;
}
*{margin:0;padding:0;box-sizing:border-box}
html,body{width:900px;height:1200px;overflow:hidden}
body{background:radial-gradient(circle at 40% 55%,var(--orange-light),var(--orange) 70%);font-family:'PT Sans Narrow',sans-serif;color:var(--ink);position:relative}
.panel{position:absolute;padding:16px 20px 0}
.burgers{left:0;top:0;width:300px;height:628px;background:var(--yellow);clip-path:polygon(0 0,100% 0,97% 93%,0 100%)}
.salads{left:0;top:622px;width:292px;height:578px;background:var(--sage);padding:16px 8px 0 20px;clip-path:polygon(0 2%,96% 0,100% 100%,0 100%)}
.salads-top{left:292px;top:0;width:276px;height:396px;background:var(--sage);padding:10px 6px 0 12px;clip-path:polygon(2% 0,100% 0,100% 97%,0 100%)}
.kids{left:292px;top:446px;width:270px;height:390px;background:var(--peach);padding:10px 18px 0 12px;clip-path:polygon(0 3%,100% 0,97% 100%,2% 96%)}
.eggs{left:290px;top:855px;width:280px;height:345px;background:var(--cream);padding:18px 6px 0 14px;clip-path:polygon(0 3%,100% 0,100% 100%,2% 100%)}
.breakfast{left:570px;top:0;width:330px;height:1200px;background:var(--cream-light);padding:36px 10px 0 17px;clip-path:polygon(0 0,100% 0,100% 100%,2% 100%)}
.section-title{font-family:'Oswald',sans-serif;font-weight:700;color:var(--red);font-size:27px;font-variant:small-caps;letter-spacing:.5px;line-height:1}
.burgers .section-title{margin:20px 0 22px}
.salads .section-title{margin:12px 0 18px}
.kids .section-title,.eggs .section-title{margin:0 0 12px 0}
.item{margin-bottom:16px}
.item-name{font-family:'Oswald',sans-serif;font-weight:500;color:var(--blue);font-size:15px;text-transform:uppercase;line-height:1.2;white-space:nowrap}
.item-name .price{margin-left:6px}
.item-name .size{font-family:'PT Sans Narrow',sans-serif;font-weight:700;font-size:10px;margin-left:6px}
.item-desc{font-size:12px;line-height:1.42}
.item-desc .option{display:block;padding-left:8px}
.burgers .item{margin-bottom:14px}
.salads .item{margin-bottom:14px}
.salads .item-name,.salads-top .item-name{font-size:14.5px}
.salads-top .item{margin-bottom:17px}
.notice{position:absolute;left:300px;top:402px;width:264px;height:20px;background:#fff;font-size:11px;line-height:20px;padding-left:6px;clip-path:polygon(0 0,100% 10%,99% 100%,0 100%)}
.kids-banner{position:absolute;left:290px;top:494px;width:238px;height:30px;background:var(--blue);color:#fff;font-size:11.5px;line-height:30px;padding-left:10px;white-space:nowrap;overflow:hidden;clip-path:polygon(0 0,100% 0,96% 100%,2% 100%)}
.kids .item{margin-bottom:14px}
.kids .spacer{height:50px}
.eggs .item{margin-bottom:13px}
.eggs .item-name{font-size:14.5px}
.breakfast .item{margin-bottom:17px}
.breakfast .item.short{margin-bottom:13px}
.breakfast .item-name{font-size:15.5px;white-space:normal}
</style>
</head>
<body>

<section class="panel burgers">
  <h2 class="section-title">Tumbler Burgers</h2>
  <div class="item"><h3 class="item-name">Hamburger<span class="price">5.95</span></h3><p class="item-desc">6 oz hand-formed patty, lettuce, tomato, red onion, mayo, on a grilled Kaiser roll</p></div>
  <div class="item"><h3 class="item-name">Cheeseburger<span class="price">6.50</span></h3><p class="item-desc">6 oz hand-formed patty, American cheddar, lettuce, tomato, red onion, mayo, on a grilled Kaiser roll</p></div>
  <div class="item" style="margin-bottom:4px"><h3 class="item-name">Bacon Cheeseburger<span class="price">7.50</span></h3><p class="item-desc">6 oz hand-formed patty, American cheddar, Ridgeback hickory-smoked bacon, lettuce, tomato, red onion, mayo, on a grilled Kaiser roll</p></div>
  <div class="item"><h3 class="item-name">Salsa Cheddar Burger<span class="price">6.75</span></h3><p class="item-desc">6 oz hand-formed patty, American cheddar, our fresh speciality salsa, lettuce, tomato, red onion, mayo, on a grilled Kaiser roll</p></div>
  <div class="item"><h3 class="item-name">Bacon Cheeseburger<span class="price">8</span></h3><p class="item-desc">6 oz hand-formed patty, crumbled blue cheese, Ridgeback hickory-smoked bacon, lettuce, tomato, red onion, mayo, on a grilled Kaiser roll</p></div>
  <div class="item"><h3 class="item-name">Mushroom Cheddar Burger<span class="price">8</span></h3><p class="item-desc">6 oz hand-formed patty, American cheddar, fresh mushroom caps, lettuce, tomato, red onion, mayo, on a grilled Kaiser roll</p></div>
  <div class="item"><h3 class="item-name">Southwest Burger<span class="price">8</span></h3><p class="item-desc">Spicy 6 oz hand-formed patty, lettuce, tomato, Monterey Jack, homemade guacamole and topped with our signature chipotle mayo dressing</p></div>
</section>

<section class="panel salads">
  <h2 class="section-title">Salads</h2>
  <div class="item"><h3 class="item-name">The Venetian<span class="size">SMALL 6.95 | LARGE 7.95</span></h3><p class="item-desc">Homemade chicken or tuna salad, tossed with romaine lettuce, tomatoes, carrots, onions, hot peppers, mushrooms and herbed oil &amp; vinegar dressing</p></div>
  <div class="item"><h3 class="item-name">C.O.S.<span class="size">SMALL 6.95 | LARGE 7.95</span></h3><p class="item-desc">Our delicious marinated chicken, grilled to succulent perfection, served over a big romaine garden salad with our homemade Caesar-Dijon dressing</p></div>
  <div class="item"><h3 class="item-name">Chef Salad<span class="size">SMALL 6.95 | LARGE 8.95</span></h3><p class="item-desc">Ham, turkey &amp; cheese over a romaine garden mix with your choice of homemade dressing</p></div>
  <div class="item"><h3 class="item-name">The Combo<span class="size">ANY TWO (2) 7.95 | ANY THREE (3) 8.95</span></h3><p class="item-desc">Our chicken, tuna and egg salad, served over a big romaine garden salad and our herbed oil &amp; vinaigrette dressing on the side</p></div>
  <div class="item"><h3 class="item-name">Pear Gorgonzola Salad<span class="size">SMALL 6.95 | LARGE 7.95</span></h3><p class="item-desc">Fresh pears and crumbed Gorgonzola cheese over a romaine medley, grilled spicy chicken, marinated in our own spicy blend, chopped walnuts and our fresh herbed oil &amp; vinaigrette dressing</p></div>
  <div class="item"><h3 class="item-name">Greek Salad<span class="size">SMALL 6.95 | LARGE 7.95</span></h3><p class="item-desc">Grilled lemon chicken, feta cheese, Greek olives, chopped red onion and our Greek vinaigrette over a romaine medley</p></div>
</section>

<section class="panel salads-top">
  <div class="item"><h3 class="item-name">Buffalo Chicken Salad<span class="size">SMALL 6.95 | LARGE 7.95</span></h3><p class="item-desc">Grilled buffalo chicken, romaine medley, Monterey Jack cheese, tomatoes, croutons and red onion with crumbled blue cheese dressing</p></div>
  <div class="item"><h3 class="item-name">Caesar's Salad<span class="size">SMALL 6.95 | LARGE 7.95</span></h3><p class="item-desc">Grilled spicy chicken over a romaine medley and our fresh Caesar dressing</p></div>
  <div class="item"><h3 class="item-name">Spinach Salad<span class="price">6.75</span></h3><p class="item-desc">Chopped hard-boiled egg, bacon bits, red onion, carrots, mushroom and our fresh herbed oil &amp; vinaigrette dressing<span class="option">with grilled chicken&nbsp;&nbsp;8.75</span></p></div>
  <div class="item"><h3 class="item-name">Southwest Salad<span class="price">7.95</span></h3><p class="item-desc">Fresh romaine medley, tomatoes, Mexican corn, crushed tortilla chips, Monterey Jack cheese blend and sliced avocados, topped with our fresh chipotle ranch dressing<span class="option">with spicy chicken&nbsp;&nbsp;9</span><span class="option">with spicy skirt steak&nbsp;&nbsp;10</span></p></div>
</section>

<p class="notice">Please check specials menu for our list of seasonal creations</p>

<section class="panel kids">
  <h2 class="section-title" style="font-size:26px">KIDS MENU</h2>
  <div class="spacer"></div>
  <div class="item"><h3 class="item-name">Grilled Cheese<span class="price">4</span></h3></div>
  <div class="item" style="margin-bottom:18px"><h3 class="item-name">Chicken Nuggets<span class="price">4</span></h3></div>
  <div class="item"><h3 class="item-name">Cheese Quesadilla<span class="price">4.50</span></h3><p class="item-desc">Grilled flour tortilla with your choice of cheese<span class="option">with chicken or steak&nbsp;&nbsp;6</span></p></div>
  <div class="item"><h3 class="item-name">Cheeseburger<span class="price">4.50</span></h3><p class="item-desc">4 oz prime beef, lettuce, tomato, red onion slice and your choice of cheese</p></div>
  <div class="item"><h3 class="item-name">Kids Fajitas<span class="price">6</span></h3><p class="item-desc">Marinated chicken or steak, sauteed peppers, caramelized onions and sour cream on the side<span class="option">with homemade guacamole&nbsp;&nbsp;7</span></p></div>
</section>
<p class="kids-banner">• Children 10 or under. Served with a bag of Crispa chips.</p>

<section class="panel eggs">
  <h2 class="section-title">Eggs</h2>
  <div class="item"><h3 class="item-name">Eggs, Taters and Toast<span class="price">5.50</span></h3><p class="item-desc">Egg-whites&nbsp;&nbsp;add 1.50</p></div>
  <div class="item"><h3 class="item-name">Egg Sandwich<span class="price">2.50</span></h3><p class="item-desc">Two-egg sandwich&nbsp;&nbsp;3.50</p></div>
  <div class="item"><h3 class="item-name">Egg and Cheese Sandwich<span class="price">3</span></h3><p class="item-desc">Two-egg and cheese sandwich&nbsp;&nbsp;4</p></div>
  <div class="item"><h3 class="item-name">Meat, Egg and Cheese Sandwich<span class="price">4.75</span></h3><p class="item-desc"><span class="option">in a bagel or wrap&nbsp;&nbsp;add .50</span></p></div>
  <div class="item"><h3 class="item-name">Egg, Cheese and Veggie Sandwich<span class="price">4.75</span></h3></div>
</section>

<section class="panel breakfast">
  <div class="item"><h3 class="item-name">Cheese Omelet with Taters &amp; Toast<span class="price">6.50</span></h3><p class="item-desc"><span class="option">veggies: (mushrooms, tomatoes, onion, broccoli, spinach, peppers, jalapenos)&nbsp;&nbsp;add .50 each</span><span class="option">egg-whites&nbsp;&nbsp;add 1.50</span></p></div>
  <div class="item"><h3 class="item-name">Breakfast Burrito<span class="price">5.95</span></h3><p class="item-desc">Large flour tortilla, filled with scrambled eggs, bacon, black beans, home fries, cheddar cheese and our homemade salsa</p></div>
  <div class="item"><h3 class="item-name">Southwest White Veggie Omelet<span class="price">10.95</span></h3><p class="item-desc">Four egg-whites with Monterey Jack cheese, tomatoes, onions, peppers, spinach and our homemade salsa, served with sliced tomatoes and toast</p></div>
  <div class="item"><h3 class="item-name">Hasta La Feasta<span class="price">7.95</span></h3><p class="item-desc">Scrambled eggs in tortillas, topped with melted cheese and our homemade salsa, served with home fries</p></div>
  <div class="item"><h3 class="item-name">Grecian Omelet<span class="price">8.95</span></h3><p class="item-desc">Spinach and feta omelet with taters and toast</p></div>
  <div class="item"><h3 class="item-name">Hunter's Omelet<span class="price">8.95</span></h3><p class="item-desc">Bacon, potato, onions and cheddar omelet with taters &amp; toast</p></div>
  <div class="item"><h3 class="item-name">Fruity French Pig Omelet<span class="price">8.95</span></h3><p class="item-desc">Ham, Brie &amp; raspberry jam omelet with taters &amp; toast</p></div>
  <div class="item"><h3 class="item-name">Western Omelet<span class="price">8.95</span></h3><p class="item-desc">Ham, cheddar, pepper and onion omelet with taters &amp; toast</p></div>
  <div class="item"><h3 class="item-name">Glutton's Paradise<span class="price">8.95</span></h3><p class="item-desc">3 eggs your way, 2 pancakes and a byproduct of your choice</p></div>
  <div class="item short"><h3 class="item-name">Buttermilk Pancakes (3)<span class="price">5.25</span></h3></div>
  <div class="item short"><h3 class="item-name">Short Stack Buttermilk Pancakes (2)<span class="price">4.25</span></h3></div>
  <div class="item short"><h3 class="item-name">French Toast (4)<span class="price">5.50</span></h3></div>
  <div class="item short"><h3 class="item-name">Short Stack French Toast (3)<span class="price">4.50</span></h3></div>
  <div class="item short"><h3 class="item-name">Upgrade to 100% Maple Syrup<span class="price">1.50</span></h3></div>
  <div class="item short"><h3 class="item-name">Ridgeback Bacon, Fenwick's Turkey Bacon, Sausage, Turkey Sausage, Corley's Pork Roll or Ham Slice<span class="price">2.75</span></h3></div>
  <div class="item short"><h3 class="item-name">Side of Home Fries<span class="price">2</span></h3></div>
  <div class="item short"><h3 class="item-name">Side of Eggs<span class="price">2.50</span></h3></div>
  <div class="item short"><h3 class="item-name">Big English Muffin<span class="price">1.25</span></h3></div>
  <div class="item short"><h3 class="item-name">Toast<span class="price">1.25</span></h3></div>
  <div class="item short"><h3 class="item-name">Grilled Yogurt Muffin<span class="price">1.75</span></h3></div>
  <div class="item short"><h3 class="item-name">Toasted Bagel<span class="price">1.50</span></h3></div>
  <div class="item short"><h3 class="item-name">Toasted Bagel with Cream Cheese<span class="price">2</span></h3></div>
  <div class="item short"><h3 class="item-name">Hearthmill Oatmeal w/ Brown Sugar &amp; Milk<span class="price">3</span></h3><p class="item-desc"><span class="option">with raisins&nbsp;&nbsp;3.50</span><span class="option">with fruit&nbsp;&nbsp;4.50</span></p></div>
  <div class="item short"><h3 class="item-name">Quinoa with Raisins and Fruit<span class="price">5</span></h3></div>
</section>

</body>
</html>
```